Lantern Petro - needs a business card

Lantern Petro is a U.S. based diesel sourcing and distribution company that supports American oil & gas fields through providing quality product and consistent services.

Target Market(s)

Oil and Gas

Contact Information for Business Card

The background of the card must be white to ensure the logo pops.

Font styles to use
Serif
Sans Serif

Colors

Designer to choose colors to be used in the design.

Requirements
Must have
• Front of Card: Tag line: Lantern Petro, Powering the Nation's Oil & Gas fields.
• Not sure if you guys do this part but just in case...
• Dale Winterholt
• Owner/CEO
• C:701.555.0148
• E:Dwinterholt@lanternpetro.com
• W:Lanternpetro.com
• Locations: Servicing the Powder River, DJ basin and Bakken formations.
• Back of Card: " Frac fueling is what we do. We understand how important diesel fuel is to your operation, which is why our main service line is Frac fueling. We assure our supply and stand by our service"

```html
<!DOCTYPE html>
<html lang="en">
<head>
<meta charset="utf-8">
<title>Lantern Petro – Business Card</title>
<link href="https://fonts.googleapis.com/css2?family=Montserrat:wght@500;600;700&family=Lato:wght@400&display=swap" rel="stylesheet">
<style>
  :root{
    --navy:#1d2d5a;
    --navy-deep:#1e2a3f;
    --red:#ed1c37;
    --red-dark:#960018;
    --ink:#333333;
    --icon-dark:#333333;
    --paper:#ffffff;
  }
  html,body{margin:0;padding:0;width:1200px;height:1200px;overflow:hidden;background:var(--paper);}
  .canvas{position:relative;width:1200px;height:1200px;}
  .card{position:absolute;top:208px;width:471px;height:784px;background:var(--paper);
        box-shadow:2px 3px 6px rgba(0,0,0,.28);overflow:hidden;}
  .card--front{left:100px;}
  .card--back{left:629px;}
  .card__art{position:absolute;inset:0;width:100%;height:100%;}
  .brand-front{position:absolute;left:0;width:100%;top:118px;text-align:center;
        font-family:'Montserrat',sans-serif;font-weight:700;font-size:30px;color:var(--paper);letter-spacing:.5px;}
  .holder{position:absolute;left:0;width:100%;top:450px;text-align:center;}
  .holder__name{font-family:'Montserrat',sans-serif;font-weight:600;font-size:30px;color:var(--navy);
        letter-spacing:-.5px;line-height:34px;text-transform:uppercase;}
  .holder__title{font-family:'Montserrat',sans-serif;font-weight:500;font-size:21px;color:var(--red);line-height:24px;}
  .contact{position:absolute;left:84px;top:555px;margin:0;padding:0;list-style:none;}
  .contact__item{position:absolute;left:0;display:flex;align-items:center;white-space:nowrap;
        font-family:'Lato',sans-serif;font-size:16px;color:var(--ink);line-height:20px;}
  .contact__icon{width:37px;height:37px;border-radius:50%;display:flex;align-items:center;justify-content:center;
        margin-right:17px;flex:none;}
  .contact__icon--red{background:var(--red);}
  .contact__icon--dark{background:var(--icon-dark);}
  .contact__icon svg{width:20px;height:20px;}
  .brand-back{position:absolute;left:0;width:100%;top:210px;text-align:center;}
  .brand-back__mark{width:84px;height:84px;border-radius:50%;background:var(--navy);margin:0 auto 18px;}
  .brand-back__name{font-family:'Montserrat',sans-serif;font-weight:700;font-size:30px;color:var(--navy);letter-spacing:1px;}
  .mission{position:absolute;left:0;width:100%;top:661px;text-align:center;margin:0;
        font-family:'Lato',sans-serif;font-size:11.6px;line-height:14.5px;color:var(--paper);}
</style>
</head>
<body>
<div class="canvas">

  <section class="card card--front">
    <svg class="card__art" viewBox="0 0 589 980" preserveAspectRatio="none" aria-hidden="true">
      <polygon points="0,0 589,0 589,95 290,382 0,248" fill="var(--navy)"/>
      <polygon points="0,250 290,382 530,288 295,500 0,255" fill="var(--red)"/>
      <polygon points="589,95 589,240 530,288 290,382" fill="var(--red-dark)"/>
      <polygon points="250,365 290,382 295,500" fill="var(--red-dark)"/>
      <polygon points="0,264 205,448 0,300" fill="var(--red-dark)"/>
      <polygon points="589,250 589,285 428,395" fill="var(--navy-deep)"/>
      <path d="M0,560 H60 a27,27 0 0 1 27,27 V600 a27,27 0 0 1 -27,27 H0 Z" fill="var(--red)"/>
      <path d="M589,560 H530 a27,27 0 0 0 -27,27 V600 a27,27 0 0 0 27,27 H589 Z" fill="var(--red)"/>
    </svg>
    <div class="brand-front">Lantern Petro</div>
    <div class="holder">
      <div class="holder__name">Dale Winterholt</div>
      <div class="holder__title">Owner / CEO</div>
    </div>
    <ul class="contact">
      <li class="contact__item" style="top:0">
        <span class="contact__icon contact__icon--red"><svg viewBox="0 0 20 20"><path d="M10 3 L2 10 H5 V17 H9 V12 H11 V17 H15 V10 H18 Z" fill="#fff"/></svg></span>
        <span>Servicing the Powder River,<br>DJ basin and Bakken formations.</span>
      </li>
      <li class="contact__item" style="top:53px">
        <span class="contact__icon contact__icon--dark"><svg viewBox="0 0 20 20"><path d="M3 3 L17 9 L10 11 L8 17 Z" fill="#fff"/></svg></span>
        <span>Dwinterholt@lanternpetro.com</span>
      </li>
      <li class="contact__item" style="top:101px">
        <span class="contact__icon contact__icon--red"><svg viewBox="0 0 20 20"><path d="M3 8 Q10 2 17 8 V10 H13 V8 H7 V10 H3 Z M5 11 H15 V17 H5 Z" fill="#fff"/><circle cx="10" cy="14" r="1.8" fill="var(--red)"/></svg></span>
        <span>701.555.0148</span>
      </li>
      <li class="contact__item" style="top:149px">
        <span class="contact__icon contact__icon--dark"><svg viewBox="0 0 20 20"><circle cx="10" cy="10" r="7" fill="none" stroke="#fff" stroke-width="1.5"/><ellipse cx="10" cy="10" rx="3" ry="7" fill="none" stroke="#fff" stroke-width="1.2"/><path d="M3 10 H17" stroke="#fff" stroke-width="1.2"/></svg></span>
        <span>Lanternpetro.com</span>
      </li>
    </ul>
  </section>

  <section class="card card--back">
    <svg class="card__art" viewBox="0 0 588 980" preserveAspectRatio="none" aria-hidden="true">
      <polygon points="0,800 294,553 588,815 588,980 0,980" fill="var(--red)"/>
      <polygon points="288,672 534,765 588,800 588,957" fill="var(--red-dark)"/>
      <polygon points="0,805 288,672 588,957 588,980 0,980" fill="var(--navy)"/>
      <polygon points="0,755 206,603 0,790" fill="var(--red-dark)"/>
      <polygon points="427,657 588,763 588,800" fill="var(--navy-deep)"/>
    </svg>
    <div class="brand-back">
      <div class="brand-back__mark"></div>
      <div class="brand-back__name">LANTERN PETRO</div>
    </div>
    <p class="mission">"Frac fueling is what we do.<br>We understand how important diesel fuel is to your operation,<br>which is why our main service line is Frac fueling.<br>We assure our supply and stand by our service".</p>
  </section>

</div>
</body>
</html>
```